Computer Company needs a Business card design

We need a business card design for our business. We assist people to transition to the QLX (Quorra Linkwave Exchange). The Australian Government-owned qlx™ network is a brand new telecommunications network currently being rolled out across Australia, giving access to a reliable broadband connection. Our niche market will predominantly be domestic customers in the 50+ age bracket. The assistance that we provide is everything from arranging the equipment, arranging the plan and contract term, appointment times, final testing of the network and any tweaks that need to be made. We basically PM the transition from start to finish. The business card design should be minimalist, should communicate loyalty and stability, should be easy to read and clearly explain what we do. We have asked for front and back. However, the back of the card does not have to include much information at all. It could be just a small design, or a repeat of our phone number. Up to you. The attached file only says what is required on the card. It does not specify where to arrange the text, what fonts to use, etc etc. As much as we would like to give you more info, due to our very limited design ability, we are not really able to send you any rough, or otherwise, designs of what we are after. Hopefully the above description is enough for you.

```html
<!DOCTYPE html>
<html lang="en">
<head>
<meta charset="utf-8">
<title>Qlx Made Easy business card</title>
<link rel="stylesheet" href="https://fonts.googleapis.com/css2?family=Montserrat:wght@400;500;700&display=swap">
<style>
  :root {
    --stage: #e9e7e4;
    --ink: #000000;
    --navy: #0b1030;
    --navy-deep: #05081c;
    --orange: #f7ae3b;
    --orange-dark: #e59a22;
    --paper: #ffffff;
    --text: #1d1d1d;
    --frame: rgba(255,255,255,0.55);
  }
  * { box-sizing: border-box; margin: 0; padding: 0; }
  html, body { width: 1200px; height: 891px; overflow: hidden; }
  body {
    background: var(--stage);
    font-family: "Montserrat", sans-serif;
    position: relative;
  }
  .card {
    position: absolute;
    width: 520px;
    height: 298px;
    top: 296px;
    overflow: hidden;
    box-shadow: 0 8px 24px rgba(0,0,0,0.18);
  }
  .card--front { left: 50px; background: var(--paper); }
  .card--back  { left: 630px; background: var(--navy-deep); }

  /* front */
  .front__brand-panel {
    position: absolute; left: 0; top: 0; width: 250px; height: 100%;
    background: var(--ink);
  }
  .brand-name {
    font-family: "Montserrat", sans-serif;
    font-weight: 500;
    color: var(--paper);
    letter-spacing: 0.5px;
  }
  .front__brand-panel .brand-name {
    position: absolute; left: 32px; top: 90px; width: 190px;
    font-size: 32px; line-height: 1.15;
  }
  .name-band {
    position: absolute; left: 232px; top: 52px; width: 288px; height: 76px;
    background: var(--orange);
    padding: 12px 0 0 26px;
    color: var(--text);
  }
  .name-band::before {
    content: ""; position: absolute; left: 0; top: -10px;
    width: 18px; height: 10px; background: var(--orange-dark);
    clip-path: polygon(0 100%, 100% 0, 100% 100%);
  }
  .holder-name { font-size: 27px; letter-spacing: 0.5px; line-height: 1.1; white-space: nowrap; }
  .holder-name .first { font-weight: 700; }
  .holder-name .last { font-weight: 400; }
  .holder-role { font-size: 13px; margin-top: 4px; }
  .contact-list {
    position: absolute; left: 272px; top: 188px; list-style: none;
    font-size: 13px; color: var(--text);
  }
  .contact-list li { display: flex; align-items: center; gap: 8px; height: 24px; white-space: nowrap; }
  .contact-list svg { width: 12px; height: 12px; flex: none; }

  /* back */
  .back__network {
    position: absolute; inset: 0;
    background: radial-gradient(ellipse at 55% 45%, #1a2250 0%, var(--navy) 45%, var(--navy-deep) 100%);
  }
  .back__frame {
    position: absolute; inset: 12px; border: 1px solid var(--frame);
  }
  .card--back .brand-name {
    position: absolute; left: 0; right: 0; top: 122px; text-align: center;
    font-size: 44px; white-space: nowrap;
  }
</style>
</head>
<body>
  <section class="card card--front" aria-label="Business card front">
    <div class="front__brand-panel">
      <div class="brand-name">Qlx Made Easy</div>
    </div>
    <div class="name-band">
      <div class="holder-name"><span class="first">REID</span> <span class="last">MADDOX</span></div>
      <div class="holder-role">General Manager</div>
    </div>
    <ul class="contact-list">
      <li>
        <svg viewBox="0 0 12 12"><path d="M3 1l2 2.5-1.2 1.3c.7 1.5 1.8 2.6 3.3 3.3L8.5 7 11 9l-1 2C5 11 1 7 1 2z" fill="var(--orange)"/></svg>
        0400555182
      </li>
      <li>
        <svg viewBox="0 0 12 12"><rect x="1" y="2.5" width="10" height="7" rx="1" fill="var(--orange)"/><path d="M1.5 3l4.5 3.5L10.5 3" stroke="#fff" fill="none"/></svg>
        reid@qlxmadeeasy.com.au
      </li>
      <li>
        <svg viewBox="0 0 12 12"><circle cx="6" cy="6" r="5" fill="var(--orange)"/><path d="M1 6h10M6 1c-2.5 3-2.5 7 0 10M6 1c2.5 3 2.5 7 0 10" stroke="#fff" stroke-width="0.8" fill="none"/></svg>
        www.qlxmadeeasy.com.au
      </li>
    </ul>
  </section>

  <section class="card card--back" aria-label="Business card back">
    <div class="back__network" role="img" aria-label="Dark navy field of connected network nodes and lines"></div>
    <div class="back__frame"></div>
    <div class="brand-name">Qlx Made Easy</div>
  </section>
</body>
</html>
```